Small consulting business needs logo and business card design

I need a logo, business card and letterhead design for a small consulting firm called Kestrawell Consulting. My customers are generally small to medium sized businesses but I have done work for major corporates and government departments. The field of consulting is strategic/business planning and program management. I have blue as the predominate colour in my current business card but I am happy to change this for the right design
Industry/Entity Type
Business

```html
<!DOCTYPE html>
<html lang="en">
<head>
<meta charset="utf-8">
<title>Kestrawell Consulting – Business Card and Letterhead</title>
<link rel="stylesheet" href="https://fonts.googleapis.com/css2?family=Questrial&display=swap">
<style>
  :root {
    --backdrop: #d4d4d4;
    --paper: #ffffff;
    --brand-blue: #2a6fb4;
    --accent-line: #3f74b8;
    --band-dark: #131517;
    --band-mid: #24272b;
    --ink: #111111;
    --ink-light: #ffffff;
  }
  * { box-sizing: border-box; margin: 0; padding: 0; }
  html, body { width: 1200px; height: 900px; overflow: hidden; }
  body {
    position: relative;
    background: var(--backdrop);
    font-family: "Questrial", sans-serif;
    color: var(--ink);
  }
  .business-card, .letterhead {
    position: absolute;
    background: var(--paper);
    overflow: hidden;
  }
  .business-card { left: 22px; top: 461px; width: 584px; height: 361px; }
  .letterhead { left: 630px; top: 39px; width: 554px; height: 779px; }

  .wordmark { position: absolute; color: var(--brand-blue); line-height: 1; }
  .wordmark__name { display: block; }
  .wordmark__tag { display: block; letter-spacing: 0.48em; }

  .business-card .wordmark { left: 33px; top: 38px; }
  .business-card .wordmark__name { font-size: 56px; }
  .business-card .wordmark__tag { font-size: 22px; margin-top: 8px; margin-left: 3px; }

  .letterhead .wordmark { left: 22px; top: 20px; }
  .letterhead .wordmark__name { font-size: 46px; }
  .letterhead .wordmark__tag { font-size: 17px; margin-top: 6px; margin-left: 3px; }

  .contact-list { position: absolute; list-style: none; }
  .contact-list li { display: flex; align-items: center; white-space: nowrap; }
  .contact-list svg { flex: none; fill: var(--brand-blue); }

  .business-card .contact-list { left: 34px; top: 218px; font-size: 16px; }
  .business-card .contact-list li { height: 20px; }
  .business-card .contact-list svg { width: 19px; height: 17px; margin-right: 5px; }

  .footer-band {
    position: absolute; left: 0; right: 0; bottom: 0;
    border-top: 3px solid var(--accent-line);
    background: linear-gradient(180deg, var(--band-mid), var(--band-dark));
  }
  .business-card .footer-band { height: 41px; }
  .letterhead .footer-band { height: 68px; }

  .letterhead .contact-list { left: 22px; top: 9px; font-size: 9px; color: var(--ink-light); }
  .letterhead .contact-list li { height: 11px; }
  .letterhead .contact-list svg { width: 10px; height: 9px; margin-right: 4px; }
</style>
</head>
<body>
  <svg width="0" height="0" style="position:absolute" aria-hidden="true">
    <defs>
      <symbol id="icon-phone" viewBox="0 0 20 18"><path d="M4 1l3 3-2 2c1 3 4 6 7 7l2-2 3 3-2 3C8 17 2 10 1 4z"/></symbol>
      <symbol id="icon-fax" viewBox="0 0 20 18"><rect x="5" y="1" width="10" height="5"/><rect x="2" y="7" width="16" height="7" rx="2"/><rect x="6" y="12" width="8" height="5"/></symbol>
      <symbol id="icon-web" viewBox="0 0 20 18"><path d="M10 1a8 8 0 100 16 8 8 0 000-16zm0 1.5c1.2 1.5 2 3.8 2 6.5s-.8 5-2 6.5C8.8 14 8 11.7 8 9s.8-5 2-6.5zM3 8.3h14v1.4H3z" fill-rule="evenodd"/></symbol>
      <symbol id="icon-mail" viewBox="0 0 20 18"><path d="M2 7l8-5 8 5v9H2z"/><path d="M3 8l7 5 7-5" fill="none" stroke="#fff" stroke-width="1.3"/></symbol>
      <symbol id="icon-home" viewBox="0 0 20 18"><path d="M10 1l9 8h-3v8h-4v-5H8v5H4V9H1z"/></symbol>
    </defs>
  </svg>

  <section class="business-card" aria-label="Business card">
    <div class="wordmark">
      <span class="wordmark__name">Kestrawell</span>
      <span class="wordmark__tag">Consulting</span>
    </div>
    <ul class="contact-list">
      <li><svg><use href="#icon-phone"/></svg>555-014-2280</li>
      <li><svg><use href="#icon-fax"/></svg>555-014-2291</li>
      <li><svg><use href="#icon-web"/></svg>www.kestrawellconsulting.com</li>
      <li><svg><use href="#icon-mail"/></svg>info@kestrawellconsulting.com</li>
      <li><svg><use href="#icon-home"/></svg>2480 Orchard Vale Rd. Linden, CA 90021</li>
    </ul>
    <div class="footer-band"></div>
  </section>

  <section class="letterhead" aria-label="Letterhead">
    <div class="wordmark">
      <span class="wordmark__name">Kestrawell</span>
      <span class="wordmark__tag">Consulting</span>
    </div>
    <div class="footer-band">
      <ul class="contact-list">
        <li><svg><use href="#icon-phone"/></svg>555-014-2280</li>
        <li><svg><use href="#icon-fax"/></svg>555-014-2291</li>
        <li><svg><use href="#icon-web"/></svg>www.kestrawellconsulting.com</li>
        <li><svg><use href="#icon-mail"/></svg>info@kestrawellconsulting.com</li>
        <li><svg><use href="#icon-home"/></svg>2480 Orchard Vale Rd. Linden, CA 90021</li>
      </ul>
    </div>
  </section>
</body>
</html>
```